Sleep Consulting Business

Hello I need a business card design with similar colors to my logo that was created. I help mom/parents whose little ones are having sleep issues. Are you able to recreate the picture with the girl sleeping onto a business card using a picture that I provide. That would be one side with my logo on top and on the other side would the following:
My name (in bigger letters than the rest. maybe written in script
title
email
website
phone
instagram
I have included color Inspo
Full Name, number, email, website, ig page

```html
<!DOCTYPE html>
<html lang="en">
<head>
<meta charset="utf-8">
<title>Quiet Hours Sleep – Business Card</title>
<link href="https://fonts.googleapis.com/css2?family=Allura&family=Poppins:wght@400;500&display=swap" rel="stylesheet">
<style>
  :root {
    --backdrop: #7d7d7d;
    --card-white: #ffffff;
    --taupe: #9d918c;
    --taupe-dark: #6f6560;
    --sand: #d8cbc0;
    --ink: #3d3a3a;
    --icon: #555555;
    --night-1: #141110;
    --night-2: #2a2420;
    --night-3: #3a2f24;
  }
  * { box-sizing: border-box; margin: 0; padding: 0; }
  html, body {
    width: 1093px; height: 1200px; overflow: hidden;
    background: var(--backdrop);
    font-family: "Poppins", sans-serif;
  }
  .card {
    position: absolute;
    left: 265px;
    width: 577px;
    height: 356px;
    border-radius: 22px;
    overflow: hidden;
    box-shadow: 2px 4px 6px rgba(0,0,0,0.45);
  }
  .card--front { top: 226px; background: var(--card-white); }
  .card--back { top: 621px; }

  .brand {
    position: absolute;
    left: 26px; top: 70px;
    display: flex; align-items: center; gap: 10px;
    color: var(--taupe);
    font-weight: 500;
    font-size: 22px;
    letter-spacing: 0.5px;
  }
  .brand__dot {
    width: 16px; height: 16px; border-radius: 50%;
    background: var(--taupe);
  }

  .holder {
    position: absolute;
    left: 340px; top: 36px;
    width: 240px;
    text-align: center;
  }
  .holder__name {
    font-family: "Allura", cursive;
    font-size: 52px;
    line-height: 1;
    color: var(--taupe);
  }
  .holder__title {
    margin-top: 2px;
    font-size: 14.5px;
    color: var(--ink);
    letter-spacing: 0.3px;
  }

  .contact {
    position: absolute;
    left: 33px; top: 200px;
    list-style: none;
    color: var(--ink);
    font-size: 16.5px;
    line-height: 21px;
  }
  .contact li { display: flex; align-items: center; gap: 7px; }
  .contact li:last-child { margin-top: 4px; }
  .contact svg { width: 15px; height: 15px; flex: none; }

  .footer-rule {
    position: absolute;
    left: 0; right: 0; top: 314px;
    height: 2px;
    background: var(--taupe-dark);
  }
  .footer-band {
    position: absolute;
    left: 0; right: 0; top: 322px; bottom: 0;
    background: var(--taupe);
  }

  .photo {
    position: absolute; inset: 0;
    background:
      radial-gradient(ellipse at 85% 25%, rgba(120,90,55,0.55), transparent 45%),
      linear-gradient(135deg, var(--night-1) 0%, var(--night-2) 55%, var(--night-3) 100%);
  }
  .back-brand {
    position: absolute; inset: 0;
    display: flex; align-items: center; justify-content: center; gap: 12px;
    color: var(--sand);
    font-weight: 500;
    font-size: 34px;
    letter-spacing: 1px;
  }
  .back-brand__dot {
    width: 22px; height: 22px; border-radius: 50%;
    background: var(--sand);
  }
</style>
</head>
<body>

<section class="card card--front">
  <div class="brand"><span class="brand__dot"></span>Quiet Hours Sleep</div>

  <div class="holder">
    <p class="holder__name">Daniel Hartley</p>
    <p class="holder__title">MANAGING DIRECTOR</p>
  </div>

  <ul class="contact">
    <li>
      <svg viewBox="0 0 16 16" fill="none" stroke="var(--icon)" stroke-width="1.6"><path d="M3 2l3 1 1 3-2 1c1 2 2 3 4 4l1-2 3 1 1 3c-5 1-12-6-11-11z"/></svg>
      055-210 348 677
    </li>
    <li>
      <svg viewBox="0 0 16 16"><rect x="1" y="3" width="14" height="10" fill="var(--icon)"/><path d="M1 3l7 6 7-6" fill="none" stroke="#fff" stroke-width="1.2"/></svg>
      hello@quiethours.com
    </li>
    <li>
      <svg viewBox="0 0 16 16" fill="none" stroke="var(--icon)" stroke-width="1.2"><circle cx="8" cy="8" r="6.5"/><ellipse cx="8" cy="8" rx="3" ry="6.5"/><path d="M1.5 8h13M2.5 5h11M2.5 11h11"/></svg>
      www.quiethoursleep.com
    </li>
    <li>
      <svg viewBox="0 0 16 16" fill="none" stroke="var(--icon)" stroke-width="1.3"><rect x="1.5" y="1.5" width="13" height="13" rx="3.5"/><circle cx="8" cy="8" r="3"/><circle cx="11.8" cy="4.2" r="0.6" fill="var(--icon)"/></svg>
      instagram.quiethours
    </li>
  </ul>

  <div class="footer-rule"></div>
  <div class="footer-band"></div>
</section>

<section class="card card--back">
  <div class="photo" role="img" aria-label="Photo of a child asleep under soft bedding in a dim room"></div>
  <div class="back-brand"><span class="back-brand__dot"></span>Quiet Hours Sleep</div>
</section>

</body>
</html>
```